Health Coaching Flyer for New Clients

I need a two-sided flyer (3.5" x 8.5" preferred or 5" x 7") to distribute to potential coaching clients. My business name is Talvery Health & Wellness Coaching. My business is focused on helping people with habit changes that contribute to their overall well-being. I would like the design colors to be gender neutral. I would like a small photo of myself near the "my name is Joan" statement. Please feel free to change the logo color to match the design.

Target Market(s)

Adults of all ages.

Font styles to use
Serif

Requirements
Must have
• Emphasize my opening question (found in health coaching brochure - attached).
• Small picture of myself near "my name is Joan" statement.
Should not have
• No light of pastel colors.

```html
<!DOCTYPE html>
<html lang="en">
<head>
<meta charset="utf-8">
<title>Talvery Health &amp; Wellness Coaching – Flyer</title>
<link rel="stylesheet" href="https://fonts.googleapis.com/css2?family=Roboto:wght@400;500;700;900&display=swap">
<style>
  :root{
    --teal:#0c978a;
    --teal-light:#3dbb9e;
    --teal-text:#0f9488;
    --white:#ffffff;
    --grey-text:#8a8a8a;
    --grey-rule:#c9c9c9;
    --mist:#eeeeee;
    --stage:#8c8c8c;
    --sky-top:#2c6fb8;
    --sky-mid:#8fb8de;
    --rock:#8b8e7a;
  }
  *{box-sizing:border-box;margin:0;padding:0}
  html,body{width:1200px;height:787px;overflow:hidden}
  body{background:var(--stage);font-family:"Roboto",Arial,sans-serif;position:relative}
  .flyer{position:absolute;top:56px;width:484px;height:677px;overflow:hidden}
  .flyer--front{left:96px;background:linear-gradient(135deg,var(--teal-light) 0%,var(--teal) 100%)}
  .flyer--back{left:618px;background:var(--white)}
  .flyer svg.art{position:absolute;left:0;top:0}

  .brand{position:absolute;color:var(--white);font-weight:900;line-height:1}
  .brand__name{display:block;font-size:34px;letter-spacing:2px}
  .brand__tag{display:block;font-size:8.5px;letter-spacing:.3px;margin-top:3px}
  .flyer--front .brand{left:20px;top:22px}

  .intro{position:absolute;left:31px;top:352px;width:418px;color:var(--white)}
  .intro__rule{width:84px;height:2px;background:var(--white);margin-bottom:14px}
  .intro__question{font-size:19.5px;font-weight:700;line-height:1.3;margin-bottom:20px;width:345px}
  .intro__body p{font-size:15.5px;line-height:1.48;text-align:justify}

  .back-title{position:absolute;left:28px;top:15px;color:var(--white);font-size:16.5px;font-weight:700}
  .traits{position:absolute;left:16px;top:74px;width:460px;list-style:none}
  .traits li{color:var(--grey-text);font-size:14px;line-height:1.22;padding:4px 12px 7px 0;border-bottom:1px solid var(--grey-rule);margin-bottom:7px}
  .traits li:last-child{border-bottom:none}
  .invite{position:absolute;left:0;top:286px;width:484px;height:160px;background:var(--mist);padding:18px 16px 0}
  .invite p{color:var(--teal-text);font-size:14px;line-height:1.2;font-weight:500;margin-bottom:16px;width:430px}
  .contact{position:absolute;left:0;top:484px;width:484px;text-align:center;color:var(--white)}
  .contact__lead{font-size:14px;line-height:1.35;font-weight:500}
  .contact__name{display:flex;align-items:center;justify-content:center;gap:16px;margin-top:12px;font-size:15px;font-weight:700}
  .contact__name::before,.contact__name::after{content:"";width:145px;height:1.5px;background:var(--white)}
  .contact__row{display:flex;justify-content:center;align-items:center;gap:22px;margin-top:10px;font-weight:700}
  .contact__phone{font-size:20px;display:flex;align-items:center;gap:8px}
  .contact__mail{font-size:16.5px;display:flex;align-items:center;gap:8px}
  .footer-arch{position:absolute;left:116px;top:610px;width:256px;height:90px;background:var(--teal);border:4px solid var(--white);border-bottom:none;border-radius:70px 70px 0 0;display:flex;justify-content:center;padding-top:22px}
  .footer-arch .brand{position:static}
  .footer-arch .brand__name{font-size:24px}
  .footer-arch .brand__tag{font-size:6.5px}
</style>
</head>
<body>

<section class="flyer flyer--front">
  <svg class="art" width="484" height="677" viewBox="0 0 484 677">
    <defs>
      <linearGradient id="sky" x1="0" y1="0" x2="0.3" y2="1">
        <stop offset="0" stop-color="var(--sky-top)"/>
        <stop offset="0.55" stop-color="var(--sky-mid)"/>
        <stop offset="1" stop-color="var(--rock)"/>
      </linearGradient>
      <linearGradient id="portrait" x1="0" y1="0" x2="1" y2="1">
        <stop offset="0" stop-color="#6b4a3a"/>
        <stop offset="1" stop-color="#c98f72"/>
      </linearGradient>
      <path id="nameCurve" d="M292,62 C330,110 360,170 420,225"/>
    </defs>
    <path role="img" aria-label="Photo of a hiker with raised arms on a mountain summit under a cloudy blue sky"
      d="M0,0 L268,0 C300,30 310,80 335,125 C360,170 410,200 484,200 L484,478 C462,425 425,378 360,342 C260,285 90,262 0,140 Z" fill="url(#sky)"/>
    <path d="M0,140 C90,262 260,285 360,342 C425,378 462,425 484,478" fill="none" stroke="#e6eaea" stroke-width="9"/>
    <path d="M268,0 C300,30 310,80 335,125 C360,170 410,200 484,200" fill="none" stroke="var(--white)" stroke-width="22" opacity="0.85"/>
    <text font-family="Roboto, Arial, sans-serif" font-size="20" font-weight="500" fill="#1b1b1b">
      <textPath href="#nameCurve">My name is Joan.</textPath>
    </text>
    <circle cx="428" cy="92" r="84" fill="var(--white)"/>
    <circle role="img" aria-label="Portrait photo of Joan" cx="428" cy="92" r="78" fill="url(#portrait)"/>
  </svg>

  <div class="brand">
    <span class="brand__name">TALVERY</span>
    <span class="brand__tag">HEALTH &amp; WELLNESS COACHING</span>
  </div>

  <div class="intro">
    <div class="intro__rule"></div>
    <h1 class="intro__question">Need support in making real, lasting lifestyle and behavior changes?</h1>
    <div class="intro__body">
      <p>I am studying to become an ALIGN-Certified Functional Health Coach.</p>
      <p>My training involves many science-based practices that improve both our health and how we grow and change as humans.</p>
      <p>I now have the opportunity to turn that knowledge into practice by coaching actual clients interested in improving their own health and well-being.</p>
    </div>
  </div>
</section>

<section class="flyer flyer--back">
  <svg class="art" width="484" height="677" viewBox="0 0 484 677">
    <path d="M0,0 L300,0 C300,30 330,55 380,52 L0,62 Z" fill="#dcdcdc"/>
    <path d="M0,0 L290,0 C285,30 300,48 340,50 C250,58 100,58 0,62 Z" fill="var(--teal)"/>
  </svg>

  <h2 class="back-title">Functional health coaches...</h2>
  <ul class="traits">
    <li>Leverage your strengths rather than focus on your weaknesses</li>
    <li>Support you in finding your own strategies and motivation for change</li>
    <li>Provide a judgment-free zone and support your autonomy</li>
    <li>Use an experimental mindset to find and develop sustainable habits</li>
    <li>Act as your accountability partner as you reach your unique health goals; whether they be improving sleep, diet, fitness, social connection, or reducing stress.</li>
  </ul>

  <div class="invite">
    <p>I would like to invite you to participate with me as a client as I continue to hone my coaching skills.&nbsp; We can develop a plan and schedule that aligns with your goals.</p>
    <p>As a way to give back to my community, I am offering new clients six free coaching sessions.&nbsp; This is a limited time offer.</p>
  </div>
  <svg class="art" width="484" height="677" viewBox="0 0 484 677" aria-hidden="true">
    <path d="M0,470 C60,425 130,415 230,435 C330,455 400,445 484,420 L484,677 L0,677 Z" fill="var(--teal)"/>
  </svg>

  <div class="contact">
    <p class="contact__lead">Please contact me.&nbsp; I’m ready to support you as you work<br>to improve your health.</p>
    <p class="contact__name">Joan Talvery</p>
    <div class="contact__row">
      <span class="contact__phone">
        <svg width="17" height="17" viewBox="0 0 24 24" aria-hidden="true"><path fill="#fff" d="M6.6 10.8a15.1 15.1 0 0 0 6.6 6.6l2.2-2.2c.3-.3.7-.4 1-.2 1.1.4 2.3.6 3.6.6.6 0 1 .4 1 1V20c0 .6-.4 1-1 1A17 17 0 0 1 3 4c0-.6.4-1 1-1h3.5c.6 0 1 .4 1 1 0 1.3.2 2.5.6 3.6.1.3 0 .7-.2 1z"/></svg>
        555-014-2273
      </span>
      <span class="contact__mail">
        <svg width="18" height="13" viewBox="0 0 18 13" aria-hidden="true"><rect x="0.5" y="0.5" width="17" height="12" fill="none" stroke="#fff"/><path d="M0.5,0.5 L9,7 L17.5,0.5" fill="none" stroke="#fff"/></svg>
        talveryhwc@example.com
      </span>
    </div>
  </div>

  <div class="footer-arch">
    <div class="brand">
      <span class="brand__name">TALVERY</span>
      <span class="brand__tag">HEALTH &amp; WELLNESS COACHING</span>
    </div>
  </div>
</section>

</body>
</html>
```